Via Lumo K

Need business cards designed. Project is an Arts Center in Hollywood. It'll include 3 live theatre, a restaurant and event space.

Target Market(s)

Across the board, young and old.

Industry/Entity Type

Entertainment

Contact Information for Business Card

Be creative. This is a creative venture that I'm building.

```html
<!DOCTYPE html>
<html lang="en">
<head>
<meta charset="utf-8">
<title>Via Lumo K — Business Card</title>
<link href="https://fonts.googleapis.com/css2?family=Bodoni+Moda:wght@400&family=Jost:wght@400&display=swap" rel="stylesheet">
<style>
  :root {
    --slate: #5f82a3;
    --ink: #3a3d42;
    --text: #55595f;
    --paper: #ffffff;
    --band: #2f3033;
    --backdrop: #e6e6e4;
    --sky-top: #7893b6;
    --sky-mid: #a9bcd2;
    --facade: #e8ebee;
    --ground: #b7bec5;
  }
  html, body {
    margin: 0;
    padding: 0;
    width: 1193px;
    height: 1200px;
    overflow: hidden;
    background: var(--backdrop);
  }
  .canvas {
    position: relative;
    width: 1193px;
    height: 1200px;
    background: var(--backdrop);
  }
  .card-set {
    position: absolute;
    left: 116px;
    top: 29px;
    width: 596px;
    height: 708px;
    transform: scale(1.611);
    transform-origin: top left;
  }
  .card {
    position: absolute;
    left: 0;
    width: 596px;
    height: 348px;
    overflow: hidden;
    background: var(--paper);
    box-shadow: 0 1px 3px rgba(0, 0, 0, 0.12);
  }
  .card-front { top: 0; }
  .card-back { top: 360px; }

  .brand-name {
    position: absolute;
    left: 72px;
    top: 112px;
    margin: 0;
    font-family: "Bodoni Moda", serif;
    font-weight: 400;
    font-size: 56px;
    line-height: 1;
    color: var(--slate);
    white-space: nowrap;
  }
  .contact-name {
    position: absolute;
    left: 330px;
    top: 181px;
    margin: 0;
    font-family: "Bodoni Moda", serif;
    font-weight: 400;
    font-size: 22px;
    line-height: 28px;
    letter-spacing: 1.2px;
    color: var(--ink);
    text-transform: uppercase;
    white-space: nowrap;
  }
  .contact-list {
    position: absolute;
    left: 330px;
    top: 229px;
    margin: 0;
    padding: 0;
    list-style: none;
    font-family: "Jost", sans-serif;
    font-size: 15.5px;
    line-height: 20px;
    color: var(--text);
    text-transform: uppercase;
  }
  .contact-list li {
    position: relative;
    padding-left: 24px;
    margin-bottom: 6px;
    white-space: nowrap;
  }
  .contact-list li.email { text-transform: none; }
  .contact-list svg {
    position: absolute;
    left: 0;
    top: 3px;
    width: 15px;
    height: 15px;
  }

  .venue-image {
    position: absolute;
    left: 0;
    top: 0;
    width: 596px;
    height: 318px;
    background: linear-gradient(160deg, var(--sky-top) 0%, var(--sky-mid) 32%, var(--facade) 58%, #d6dbe0 80%, var(--ground) 100%);
  }
  .back-brand {
    position: absolute;
    left: 22px;
    top: 112px;
    margin: 0;
    font-family: "Bodoni Moda", serif;
    font-weight: 400;
    font-size: 56px;
    line-height: 1;
    color: var(--paper);
    white-space: nowrap;
  }
  .tagline-band {
    position: absolute;
    left: 0;
    top: 318px;
    width: 596px;
    height: 30px;
    background: var(--band);
  }
  .tagline {
    position: absolute;
    right: 30px;
    top: 0;
    margin: 0;
    font-family: "Jost", sans-serif;
    font-size: 15.5px;
    line-height: 30px;
    color: var(--paper);
    text-transform: uppercase;
    white-space: nowrap;
  }
</style>
</head>
<body>
<main class="canvas">
  <div class="card-set">
    <section class="card card-front" aria-label="Card front">
      <p class="brand-name">Via Lumo K</p>
      <h1 class="contact-name">Daniel Moreau</h1>
      <ul class="contact-list">
        <li class="address">
          <svg viewBox="0 0 16 16" aria-hidden="true"><circle cx="8" cy="8" r="8" fill="var(--slate)"/><path d="M8 3.2a3 3 0 0 0-3 3c0 2.2 3 6 3 6s3-3.8 3-6a3 3 0 0 0-3-3z" fill="#fff"/><circle cx="8" cy="6.2" r="1.1" fill="var(--slate)"/></svg>
          415 N. Larkmere Ave.<br>Los Angeles, CA 90046
        </li>
        <li class="phone">
          <svg viewBox="0 0 16 16" aria-hidden="true"><circle cx="8" cy="8" r="8" fill="var(--slate)"/><path d="M5.3 4.2l1.4-.3.8 2-.9.8a5 5 0 0 0 2.7 2.7l.8-.9 2 .8-.3 1.4c-3.6.4-6.9-2.9-6.5-6.5z" fill="#fff"/></svg>
          323.555.0148
        </li>
        <li class="email">
          <svg viewBox="0 0 16 16" aria-hidden="true"><circle cx="8" cy="8" r="8" fill="var(--slate)"/><rect x="4" y="5.2" width="8" height="5.6" rx="0.6" fill="#fff"/><path d="M4.3 5.6L8 8.4l3.7-2.8" fill="none" stroke="var(--slate)" stroke-width="0.9"/></svg>
          dmoreau@vialumok.com
        </li>
      </ul>
    </section>

    <section class="card card-back" aria-label="Card back">
      <div class="venue-image" role="img" aria-label="Architectural rendering of the white arts center building under a blue sky, with palm trees, outdoor seating and large black-and-white film stills on its facade"></div>
      <p class="back-brand">Via Lumo K</p>
      <div class="tagline-band">
        <p class="tagline">Live Theatre, a Restaurant and Event Space</p>
      </div>
    </section>
  </div>
</main>
</body>
</html>
```